Design Creative Banner or Gif Ads. 3 Designs To Be Selected

Come up with some creative banner ads for stonewell.co.nz

*At least 3 different winning banners will be chosen*

Please provide banner ads / gif ads in common google ads / website banner formats.

They can be gif or static but must stand out while still maintaining clear clean text and visuals, with a premium professional feel (please avoid clip art or anything that gives a cheap message).

Please keep in mind that these will likely be small ads so text needs to be large and if there's there a lot of text then use multiple frames/ pages as submit as a gif.

Style
Minimal & clean lines
Architectural or realistic images
Avoid cartoon styles, clipart, or anything that looks cheap

Font
Nexa or Montserrat or similar

Tone
Premium, serious, trustworthy — fits new builds

Colours
Option 1: Deep Navy (trust & quality) & lighter blues and warm grey
Option 2: Open to bright colours to help the ads stand out, such as (but not limited to) bright pink with black, yellow, fluorescent green, provided the messaging is still done professionally.
Our logo is attached (Stone Well Logo)

Display Sizes
Ad specs for file sizes should be file formats like JPEG, GIF, and PNG, with animations limited to a max of 30 seconds or less.
We will need several different ad sizes provided for each of the 3 selected winning designs.

• Medium Rectangle: 300 × 250 pixels
• Leaderboard: 728 × 90 pixels
• Desktop Banner ad image: (640x360 pixels)
• Desktop Banner ad image 2: (300x600 pixels)
• Possibly one or two other sizes

Flexibility to be creative
The ad text, words, upper/lower case, layout, colour, theme, and images can be adjusted to how you think it will look best. The follow example ads are just examples of what we are after but we are keen to see what you can create.

Recommendations at this point:
1. Avoid text heavy
2. Looking for more Gif ads
3. Imaging: if possible use real stock photo's rather than AI

Themes:

1
Building Soon? Start Here
Free Build Planning Pack:
✓ Build Cost Calculator
✓ Hidden Cost Checklist
✓ Builder Comparison Guide
Build With Confidence
Download Free

2
Before You Choose A Builder
Compare Price, Scope, Risk & Value
Avoid Costly Mistakes
Choose The Right Builder With Confidence
Download The Free Guide

3
Planning A New Build?
Avoid These Common Mistakes:
✗ Hidden Exclusions
✗ Missing Scope
✗ Unrealistic Allowances
✗ Budget Blowouts
Download The Free Guide

4
Before You Buy Land
Know what it could cost to build.
Avoid Costly Building Mistakes
Download Our Free Guides

5
Know Your Build Budget?
• Free Build Cost Calculator
• Hidden Cost Checklist
• Build Planning Tools
Calculate Costs (Download)

Target Market(s)

Landowners looking to build

Industry/Entity Type

Building

Font styles to use
Other font styles liked:
• Nexa or Montserrat or similar

Requirements
Should not have
• Avoid cartoon styles, clipart, or anything that looks cheap

```html
<!DOCTYPE html>
<html lang="en">
<head>
<meta charset="utf-8">
<title>Stone Well – Display Ad Set</title>
<link rel="stylesheet" href="https://fonts.googleapis.com/css2?family=Oswald:wght@500&family=Poppins:wght@400;500;600;800&display=swap">
<style>
  :root {
    --navy: #0b3350;
    --blue: #2e8fc0;
    --blue-light: #4aa8d6;
    --white: #ffffff;
    --canvas: #eeebe6;
    --photo-a: #e9ebee;
    --photo-b: #9aa3ad;
    --rule: rgba(255,255,255,0.25);
  }
  * { box-sizing: border-box; margin: 0; padding: 0; }
  html, body { width: 794px; height: 1200px; overflow: hidden; }
  body { background: var(--canvas); position: relative; font-family: "Poppins", sans-serif; color: var(--white); }

  .ad { position: absolute; background: var(--navy); overflow: hidden; box-shadow: 0 2px 6px rgba(0,0,0,0.18); }
  .photo { position: absolute; background: linear-gradient(135deg, var(--photo-a) 0%, #d3d7dc 55%, var(--photo-b) 100%); }
  .wave { position: absolute; display: block; }
  .copy { position: absolute; display: flex; flex-direction: column; align-items: center; justify-content: center; text-align: center; }
  .kicker { font-family: "Oswald", sans-serif; font-weight: 500; line-height: 1.1; letter-spacing: -0.3px; white-space: nowrap; }
  .headline { font-weight: 800; line-height: 1.02; text-transform: uppercase; white-space: nowrap; }
  .rule { width: 84%; height: 1px; background: var(--rule); }
  .support { font-weight: 400; line-height: 1.2; white-space: nowrap; }

  .footer { position: absolute; left: 0; right: 0; bottom: 0; background: var(--white); display: flex; align-items: center; }
  .brand { display: flex; align-items: center; }
  .brand-mark { background: var(--navy); flex: none; }
  .brand-text { display: flex; flex-direction: column; }
  .brand-name { font-weight: 600; line-height: 1; color: var(--navy); white-space: nowrap; }
  .brand-tag { display: block; margin-top: 2px; overflow: visible; }
  .brand-tag text { font-family: "Poppins", sans-serif; font-weight: 500; font-size: 8px; fill: var(--blue); }

  .cta { background: linear-gradient(180deg, var(--blue-light), var(--blue)); color: var(--white); border-radius: 3px; display: flex; flex-direction: column; align-items: center; justify-content: center; text-align: center; line-height: 1; white-space: nowrap; box-shadow: 0 3px 4px rgba(0,0,0,0.18); }
  .cta strong { font-weight: 800; }

  .ad-desktop { left: 89px; top: 80px; width: 559px; height: 314px; }
  .ad-leader { left: 88px; top: 424px; width: 408px; height: 52px; }
  .ad-leader-lg { left: 87px; top: 498px; width: 635px; height: 78px; }
  .split-rule { position: absolute; top: 0; bottom: 0; width: 1px; background: var(--rule); }
  .side-panel { position: absolute; top: 0; right: 0; bottom: 0; background: var(--white); display: flex; flex-direction: column; align-items: center; justify-content: center; }

  .ad-sky { left: 89px; top: 604px; width: 261px; height: 523px; }
  .sky-header { position: absolute; left: 0; top: 0; width: 100%; height: 63px; background: var(--white); display: flex; justify-content: center; align-items: center; }
  .sky-notch { position: absolute; left: 122px; top: 62px; width: 0; height: 0; border-left: 7px solid transparent; border-right: 7px solid transparent; border-top: 6px solid var(--white); }

  .ad-rect { left: 379px; top: 604px; width: 262px; height: 218px; }
  .ad-rect-lg { left: 379px; top: 843px; width: 293px; height: 244px; }
</style>
</head>
<body>

<!-- Desktop banner -->
<section class="ad ad-desktop" aria-label="Desktop banner">
  <div class="photo" style="left:0;top:0;width:340px;height:243px" role="img" aria-label="Overhead photo of hands working over house plans with a ruler, calculator and notepad"></div>
  <svg class="wave" style="left:0;top:0" width="559" height="243" viewBox="0 0 559 243" aria-hidden="true">
    <path d="M290 0 L302 0 Q292 140 258 243 L243 243 Q280 140 290 0 Z" fill="var(--blue)"/>
    <path d="M302 0 L559 0 L559 243 L258 243 Q292 140 302 0 Z" fill="var(--navy)"/>
  </svg>
  <div class="copy" style="left:305px;top:22px;width:235px;height:200px">
    <p class="kicker" style="font-size:19px">Before You Choose A Builder</p>
    <p class="headline" style="font-size:28px;margin-top:2px">Compare<br>Price, Scope,<br>Risk &amp; Value</p>
    <span class="rule" style="margin:8px 0 10px"></span>
    <p class="support" style="font-size:17px">Avoid Costly Mistakes<br>Choose The Right Builder<br>With Confidence</p>
  </div>
  <div class="footer" style="height:71px;padding-left:19px">
    <div class="brand">
      <span class="brand-mark" style="width:40px;height:40px;margin-right:30px"></span>
      <div class="brand-text"><span class="brand-name" style="font-size:25px">Stone Well</span><svg class="brand-tag" width="171" height="7" viewBox="0 0 200 8"><text x="0" y="7" textLength="200" lengthAdjust="spacingAndGlyphs">COMPARE QUOTES FROM TRUSTED BUILDERS</text></svg></div>
    </div>
    <a class="cta" style="position:absolute;left:275px;top:14px;width:268px;height:36px;font-size:19px">Download The Free Guide</a>
  </div>
</section>

<!-- Leaderboard small -->
<section class="ad ad-leader" aria-label="Leaderboard banner">
  <div class="copy" style="left:0;top:0;width:137px;height:52px">
    <p class="kicker" style="font-size:8.5px">Before You Choose A Builder</p>
    <p class="headline" style="font-size:11px;margin-top:1px">Compare Price,<br>Scope, Risk &amp; Value</p>
  </div>
  <span class="split-rule" style="left:137px"></span>
  <div class="copy" style="left:137px;top:0;width:82px;height:52px">
    <p class="support" style="font-size:7px">Avoid Costly<br>Mistakes Choose The<br>Right Builder<br>With Confidence</p>
  </div>
  <div class="photo" style="left:222px;top:0;width:110px;height:52px" role="img" aria-label="Photo of a team reviewing house plans with a hard hat and calculator"></div>
  <svg class="wave" style="left:216px;top:0" width="30" height="52" viewBox="0 0 30 52" aria-hidden="true">
    <path d="M0 0 L10 0 Q12 30 30 52 L0 52 Z" fill="var(--navy)"/>
    <path d="M10 0 L14 0 Q16 30 30 52 L26 52 Q10 30 10 0 Z" fill="var(--blue)"/>
  </svg>
  <div class="side-panel" style="width:76px">
    <div class="brand" style="margin-bottom:5px">
      <span class="brand-mark" style="width:9px;height:9px;margin-right:5px"></span>
      <div class="brand-text"><span class="brand-name" style="font-size:8px">Stone Well</span><svg class="brand-tag" width="45" height="2" viewBox="0 0 200 8" style="margin-top:1px"><text x="0" y="7" textLength="200" lengthAdjust="spacingAndGlyphs">COMPARE QUOTES FROM TRUSTED BUILDERS</text></svg></div>
    </div>
    <a class="cta" style="width:61px;height:21px;font-size:6.5px"><span>Download The</span><strong style="font-size:9px">Free Guide</strong></a>
  </div>
</section>

<!-- Leaderboard large -->
<section class="ad ad-leader-lg" aria-label="Large leaderboard banner">
  <div class="copy" style="left:0;top:0;width:213px;height:78px">
    <p class="kicker" style="font-size:13px">Before You Choose A Builder</p>
    <p class="headline" style="font-size:16.5px;margin-top:2px">Compare Price,<br>Scope, Risk &amp; Value</p>
  </div>
  <span class="split-rule" style="left:213px"></span>
  <div class="copy" style="left:213px;top:0;width:125px;height:78px">
    <p class="support" style="font-size:11px">Avoid Costly<br>Mistakes Choose The<br>Right Builder<br>With Confidence</p>
  </div>
  <div class="photo" style="left:345px;top:0;width:170px;height:78px" role="img" aria-label="Photo of a team reviewing house plans with a hard hat and calculator"></div>
  <svg class="wave" style="left:335px;top:0" width="45" height="78" viewBox="0 0 45 78" aria-hidden="true">
    <path d="M0 0 L10 0 Q14 45 45 78 L0 78 Z" fill="var(--navy)"/>
    <path d="M10 0 L16 0 Q20 45 45 78 L38 78 Q12 45 10 0 Z" fill="var(--blue)"/>
  </svg>
  <div class="side-panel" style="width:120px">
    <div class="brand" style="margin-bottom:8px">
      <span class="brand-mark" style="width:14px;height:14px;margin-right:8px"></span>
      <div class="brand-text"><span class="brand-name" style="font-size:12px">Stone Well</span><svg class="brand-tag" width="70" height="3" viewBox="0 0 200 8" style="margin-top:1px"><text x="0" y="7" textLength="200" lengthAdjust="spacingAndGlyphs">COMPARE QUOTES FROM TRUSTED BUILDERS</text></svg></div>
    </div>
    <a class="cta" style="width:93px;height:32px;font-size:10px"><span>Download The</span><strong style="font-size:13px">Free Guide</strong></a>
  </div>
</section>

<!-- Skyscraper -->
<section class="ad ad-sky" aria-label="Skyscraper banner">
  <div class="sky-header">
    <div class="brand">
      <span class="brand-mark" style="width:28px;height:28px;margin-right:14px"></span>
      <div class="brand-text"><span class="brand-name" style="font-size:20px">Stone Well</span><svg class="brand-tag" width="132" height="5" viewBox="0 0 200 8"><text x="0" y="7" textLength="200" lengthAdjust="spacingAndGlyphs">COMPARE QUOTES FROM TRUSTED BUILDERS</text></svg></div>
    </div>
  </div>
  <span class="sky-notch"></span>
  <div class="photo" style="left:0;top:270px;width:261px;height:253px" role="img" aria-label="Overhead photo of hands working over house plans with a ruler, calculator and notepad"></div>
  <svg class="wave" style="left:0;top:270px" width="261" height="80" viewBox="0 0 261 80" aria-hidden="true">
    <path d="M0 0 L261 0 L261 55 Q140 10 0 12 Z" fill="var(--navy)"/>
    <path d="M0 12 Q140 10 261 55 L261 63 Q140 20 0 20 Z" fill="var(--blue)"/>
  </svg>
  <div class="copy" style="left:0;top:68px;width:261px;height:210px">
    <p class="kicker" style="font-size:20px">Before You Choose A Builder</p>
    <p class="headline" style="font-size:30px;margin-top:3px">Compare<br>Price, Scope,<br>Risk &amp; Value</p>
    <span class="rule" style="margin:9px 0 10px"></span>
    <p class="support" style="font-size:16px">Avoid Costly Mistakes<br>Choose The Right Builder<br>With Confidence</p>
  </div>
  <a class="cta" style="position:absolute;left:33px;top:476px;width:210px;height:28px;font-size:15px">Download The Free Guide</a>
</section>

<!-- Medium rectangle -->
<section class="ad ad-rect" aria-label="Medium rectangle banner">
  <div class="photo" style="left:0;top:0;width:140px;height:172px" role="img" aria-label="Overhead photo of hands working over house plans with a ruler and calculator"></div>
  <svg class="wave" style="left:0;top:0" width="262" height="172" viewBox="0 0 262 172" aria-hidden="true">
    <path d="M126 0 L134 0 Q122 100 110 172 L102 172 Q114 100 126 0 Z" fill="var(--blue)"/>
    <path d="M134 0 L262 0 L262 172 L110 172 Q122 100 134 0 Z" fill="var(--navy)"/>
  </svg>
  <div class="copy" style="left:128px;top:10px;width:132px;height:155px">
    <p class="kicker" style="font-size:11px">Before You Choose A Builder</p>
    <p class="headline" style="font-size:15px;margin-top:1px">Compare<br>Price, Scope,<br>Risk &amp; Value</p>
    <span class="rule" style="margin:6px 0 6px"></span>
    <p class="support" style="font-size:11px">Avoid Costly<br>Mistakes Choose The<br>Right Builder<br>With Confidence</p>
  </div>
  <div class="footer" style="height:46px;padding-left:11px">
    <div class="brand">
      <span class="brand-mark" style="width:20px;height:20px;margin-right:10px"></span>
      <div class="brand-text"><span class="brand-name" style="font-size:14px">Stone Well</span><svg class="brand-tag" width="95" height="4" viewBox="0 0 200 8"><text x="0" y="7" textLength="200" lengthAdjust="spacingAndGlyphs">COMPARE QUOTES FROM TRUSTED BUILDERS</text></svg></div>
    </div>
    <a class="cta" style="position:absolute;left:155px;top:6px;width:93px;height:32px;font-size:10px"><span>Download The</span><strong style="font-size:13px">Free Guide</strong></a>
  </div>
</section>

<!-- Medium rectangle large -->
<section class="ad ad-rect-lg" aria-label="Large rectangle banner">
  <div class="photo" style="left:0;top:0;width:160px;height:192px" role="img" aria-label="Overhead photo of hands working over house plans with a ruler and calculator"></div>
  <svg class="wave" style="left:0;top:0" width="293" height="192" viewBox="0 0 293 192" aria-hidden="true">
    <path d="M140 0 L150 0 Q134 110 120 192 L110 192 Q126 110 140 0 Z" fill="var(--blue)"/>
    <path d="M150 0 L293 0 L293 192 L120 192 Q134 110 150 0 Z" fill="var(--navy)"/>
  </svg>
  <div class="copy" style="left:143px;top:12px;width:148px;height:172px">
    <p class="kicker" style="font-size:12.5px">Before You Choose A Builder</p>
    <p class="headline" style="font-size:17px;margin-top:2px">Compare<br>Price, Scope,<br>Risk &amp; Value</p>
    <span class="rule" style="margin:7px 0 7px"></span>
    <p class="support" style="font-size:12.5px">Avoid Costly<br>Mistakes Choose The<br>Right Builder<br>With Confidence</p>
  </div>
  <div class="footer" style="height:52px;padding-left:12px">
    <div class="brand">
      <span class="brand-mark" style="width:22px;height:22px;margin-right:12px"></span>
      <div class="brand-text"><span class="brand-name" style="font-size:15.5px">Stone Well</span><svg class="brand-tag" width="106" height="4" viewBox="0 0 200 8"><text x="0" y="7" textLength="200" lengthAdjust="spacingAndGlyphs">COMPARE QUOTES FROM TRUSTED BUILDERS</text></svg></div>
    </div>
    <a class="cta" style="position:absolute;left:174px;top:7px;width:104px;height:35px;font-size:11px"><span>Download The</span><strong style="font-size:14.5px">Free Guide</strong></a>
  </div>
</section>

</body>
</html>
```